Permanent Makeup (cosmetics salon) Brochure

We need a 2-4 sites brochure for our Permanent Makeup (cosmetics salon). Our company is based in Austria / Vienna. -> Our homepage is www.mk-lorenzhuber.at
This brochure should show which treatments we provide ot our customers.

I've uploaded our old brochure, the content (text) would be nearly the same (look form "Must Haves", pics have to be new (look uploaded pics)
The old brochure is to dark. -> look for our homepage maybe you can make it like this

Target Market(s)

woman, age 25-70 years who wants to have permanent makeup on eyebrows, lips or eyeliner

Industry/Entity Type

Beauty Salon

Requirements
Must have
• pics which are uploaded.

*This text (somithing about our business)
"Für Frau Lorenzhuber ist Permanent Makeup ein Kunsthandwerk. Das Team von MK-Lorenzhuber ist spezialisiert auf natürliches Permanent Makeup damit der individuelle Typ jeder Kundin am schönsten zum Ausdruck kommt."

*We do this treatments: (english)
+ Augenbrauen Microblading (eyebrows)
+ Augenbrauen Permanent Makeup (eyebrows2)
+ Lidstrich Permanent Makeup (eyeliner)
+ Lip Blushing (lips)
+ Lippen Permanent Makeup (lips2)

* Our addresses (2 locations)
Wien
Kerngasse 7b/12, 1010 Wien
Tel: 01/5827316

Villach
Birkenhofweg 24, 9524 St. Ulrich
Tel: 0676/3158940

Mail: info@mk-lorenzhuber.at
www.mk-lorenzhuber.at

```html
<!DOCTYPE html>
<html lang="de">
<head>
<meta charset="utf-8">
<title>MK-Lorenzhuber – Broschüre</title>
<link rel="stylesheet" href="https://fonts.googleapis.com/css2?family=Josefin+Sans:wght@300;400;600;700&family=Montserrat:wght@700&display=swap">
<style>
  :root {
    --stage: #2a2a2a;
    --navy: #3a4858;
    --navy-deep: #27313c;
    --gold: #e2bc4f;
    --white: #ffffff;
    --paper: #f7f7f7;
    --ink: #1f2226;
    --ring: #dadada;
  }
  * { box-sizing: border-box; margin: 0; padding: 0; }
  html, body { width: 1067px; height: 1200px; overflow: hidden; }
  body {
    background: var(--stage);
    font-family: "Josefin Sans", sans-serif;
    position: relative;
    color: var(--ink);
  }
  .view-label {
    position: absolute; left: 0; width: 1067px; text-align: center;
    color: var(--white); font-weight: 700; font-size: 25px;
  }
  .view-label--outside { top: 46px; }
  .view-label--inside { top: 1134px; }

  .spread {
    position: absolute; left: 45px; width: 973px; height: 487px;
    display: flex; box-shadow: 0 3px 10px rgba(0,0,0,.45);
  }
  .spread--outside { top: 103px; }
  .spread--inside { top: 620px; }
  .page { position: relative; width: 486.5px; height: 487px; overflow: hidden; }
  .page--dark { background: var(--navy); color: var(--white); }
  .page--light { background: var(--paper); }

  .url-band {
    position: absolute; left: 0; right: 0; top: 446px; height: 25px;
    background: var(--navy-deep); color: var(--gold);
    font-size: 13.5px; line-height: 27px; letter-spacing: .2px; text-align: center;
  }
  .page-foot { position: absolute; left: 0; right: 0; top: 471px; height: 16px; background: var(--white); }

  .brand { position: absolute; text-align: center; }
  .brand__row { display: flex; align-items: center; justify-content: center; gap: 10px; }
  .brand__dot { width: 22px; height: 22px; border-radius: 50%; border: 2px solid var(--gold); flex: none; }
  .brand__name { font-size: 19px; font-weight: 400; letter-spacing: .5px; white-space: nowrap; }
  .brand__tagline {
    font-family: "Montserrat", sans-serif; font-weight: 700;
    font-size: 6.8px; letter-spacing: 1.4px; margin-top: 9px; white-space: nowrap;
  }
  .page--dark .brand__name, .page--dark .brand__tagline { color: var(--white); }
  .page--light .brand__name, .page--light .brand__tagline { color: var(--ink); }

  /* outside back */
  .back .brand { left: 0; right: 0; top: 206px; }
  .contact-icons { position: absolute; top: 277px; left: 0; right: 0; display: flex; justify-content: center; gap: 6px; }
  .contact-icons svg { width: 22px; height: 22px; }
  .locations { position: absolute; top: 310px; left: 0; right: 0; text-align: center; font-size: 10.5px; line-height: 13px; font-weight: 300; }
  .location__city { color: var(--gold); font-weight: 700; font-size: 10.5px; }
  .location { margin-bottom: 12px; }

  /* outside front */
  .cover-photo {
    position: absolute; left: 240px; top: 0; width: 247px; height: 487px;
    background: radial-gradient(ellipse at 55% 45%, #e7b596 0%, #c98a66 45%, #8a5a45 100%);
  }
  .headline {
    position: absolute; left: 0; width: 250px; top: 108px; text-align: center;
    font-size: 34px; line-height: 40px; font-weight: 400; color: var(--white);
  }
  .headline__accent { color: var(--gold); }
  .cover .brand { left: 0; width: 256px; top: 386px; }
  .cover .brand__name { font-size: 17px; }
  .cover .url-band { width: 265px; }

  /* inside left */
  .photo { position: absolute; top: 0; height: 217px; }
  .photo--lips { left: 0; width: 331px; background: radial-gradient(ellipse at 50% 55%, #e58c8f 0%, #dfa397 35%, #f0c9b6 80%); }
  .photo--eye { left: 335px; width: 152px; background: radial-gradient(ellipse at 55% 55%, #8a6a4e 0%, #d9b5a0 40%, #efd6c8 100%); }
  .intro { position: absolute; top: 238px; left: 0; right: 0; text-align: center; }
  .intro__lead { font-size: 17px; line-height: 22px; font-weight: 400; }
  .intro__accent { color: var(--gold); font-weight: 700; font-size: 18px; line-height: 22px; letter-spacing: .5px; }
  .intro__body { margin: 12px auto 0; width: 420px; font-size: 11.6px; line-height: 16px; font-weight: 400; }
  .intro-page .brand { left: 0; right: 0; top: 392px; }
  .intro-page .brand__name { font-size: 16px; }
  .intro-page .brand__dot { width: 20px; height: 20px; }
  .intro-page .brand__tagline { margin-top: 7px; font-size: 6px; }

  /* inside right */
  .photo--portrait { left: 0; width: 487px; background: linear-gradient(90deg, #e9e3d8 0%, #f1d4b8 35%, #e8ae8c 70%, #c97a56 100%); }
  .ring {
    position: absolute; left: 298px; top: 231px; width: 224px; height: 224px;
    border-radius: 50%; border: 12px solid var(--ring);
  }
  .services-page .brand { left: 33px; top: 256px; text-align: left; }
  .services-page .brand__row { justify-content: flex-start; }
  .services-page .brand__name { font-size: 18px; }
  .treatments { position: absolute; left: 33px; top: 330px; list-style: none; font-size: 11.2px; line-height: 15.8px; }
  .treatments li::before { content: "+ "; }
</style>
</head>
<body>

<div class="view-label view-label--outside">Outside</div>

<section class="spread spread--outside">
  <div class="page page--dark back">
    <div class="brand">
      <div class="brand__row"><span class="brand__dot"></span><span class="brand__name">Marlene Lorenzhuber</span></div>
      <div class="brand__tagline">NATÜRLICHE SCHÖNHEIT MIT SORGFALT UND HINGABE</div>
    </div>
    <div class="contact-icons">
      <svg viewBox="0 0 22 22" aria-label="Adresse"><circle cx="11" cy="11" r="10" fill="none" stroke="#e2bc4f" stroke-width="1.2"/><path d="M11 5.5a3.5 3.5 0 0 0-3.5 3.5c0 2.6 3.5 6.5 3.5 6.5s3.5-3.9 3.5-6.5A3.5 3.5 0 0 0 11 5.5z" fill="#e2bc4f"/><circle cx="11" cy="9" r="1.2" fill="#3a4858"/></svg>
      <svg viewBox="0 0 22 22" aria-label="Telefon"><circle cx="11" cy="11" r="10" fill="none" stroke="#e2bc4f" stroke-width="1.2"/><path d="M8 6.5l1.6 2.2-1 1.1a6 6 0 0 0 2.7 2.7l1.1-1 2.2 1.6-1 1.6c-3.2 0-6.8-3.6-6.8-6.8z" fill="none" stroke="#e2bc4f" stroke-width="1.1"/></svg>
      <svg viewBox="0 0 22 22" aria-label="E-Mail"><circle cx="11" cy="11" r="10" fill="none" stroke="#e2bc4f" stroke-width="1.2"/><rect x="6" y="7.5" width="10" height="7" fill="#e2bc4f"/><path d="M6 7.5l5 4 5-4" fill="none" stroke="#3a4858" stroke-width=".9"/></svg>
      <svg viewBox="0 0 22 22" aria-label="Webseite"><circle cx="11" cy="11" r="10" fill="none" stroke="#e2bc4f" stroke-width="1.2"/><circle cx="11" cy="11" r="5" fill="none" stroke="#e2bc4f"/><ellipse cx="11" cy="11" rx="2.2" ry="5" fill="none" stroke="#e2bc4f"/><path d="M6 11h10M7 8.5h8M7 13.5h8" stroke="#e2bc4f" stroke-width=".8"/></svg>
    </div>
    <div class="locations">
      <div class="location"><div class="location__city">WIEN</div>Kerngasse 7b/12, 1010 Wien<br>Tel: 01/5827316</div>
      <div class="location"><div class="location__city">VILLACH</div>Birkenhofweg 24, 9524 St. Ulrich<br>Tel: 0676/3158940</div>
      <div class="location">info@mk-lorenzhuber.at</div>
    </div>
    <div class="url-band">WWW.MK-LORENZHUBER.AT</div>
  </div>

  <div class="page page--dark cover">
    <div class="cover-photo" role="img" aria-label="Portraitfoto einer jungen Frau mit natürlichem Make-up, Hand am Kinn"></div>
    <h1 class="headline"><span class="headline__accent">SCHÖNHEIT</span><br>KOMMT<br>NICHT NUR<br>VON<br>INNEN</h1>
    <div class="brand">
      <div class="brand__row"><span class="brand__dot"></span><span class="brand__name">Marlene Lorenzhuber</span></div>
      <div class="brand__tagline">NATÜRLICHE SCHÖNHEIT MIT SORGFALT UND HINGABE</div>
    </div>
    <div class="url-band">WWW.MK-LORENZHUBER.AT</div>
  </div>
</section>

<section class="spread spread--inside">
  <div class="page page--light intro-page">
    <div class="photo photo--lips" role="img" aria-label="Nahaufnahme von Lippen mit Lip Blushing"></div>
    <div class="photo photo--eye" role="img" aria-label="Nahaufnahme eines Auges mit Augenbraue und Lidstrich"></div>
    <div class="intro">
      <p class="intro__lead">Macht jeden Augenblick zu<br>EINER</p>
      <p class="intro__accent">AUGENWEIDE</p>
      <p class="intro__body">Für Frau Lorenzhuber ist Permanent Makeup ein Kunsthandwerk. Das Team von MK-Lorenzhuber ist spezialisiert auf natürliches Permanent Makeup damit der individuelle Typ jeder Kundin am schönsten zum Ausdruck kommt.</p>
    </div>
    <div class="brand">
      <div class="brand__row"><span class="brand__dot"></span><span class="brand__name">Marlene Lorenzhuber</span></div>
      <div class="brand__tagline">NATÜRLICHE SCHÖNHEIT MIT SORGFALT UND HINGABE</div>
    </div>
    <div class="url-band">WWW.MK-LORENZHUBER.AT</div>
    <div class="page-foot"></div>
  </div>

  <div class="page page--light services-page">
    <div class="photo photo--portrait" role="img" aria-label="Nahaufnahme eines Frauengesichts mit blondem Haar, Augenbraue und Lidschatten"></div>
    <div class="url-band">WWW.MK-LORENZHUBER.AT</div>
    <div class="page-foot"></div>
    <div class="ring"></div>
    <div class="brand">
      <div class="brand__row"><span class="brand__dot"></span><span class="brand__name">Marlene Lorenzhuber</span></div>
      <div class="brand__tagline">NATÜRLICHE SCHÖNHEIT MIT SORGFALT UND HINGABE</div>
    </div>
    <ul class="treatments">
      <li>Augenbrauen Microblading (eyebrows)</li>
      <li>Augenbrauen Permanent Makeup (eyebrows2)</li>
      <li>Lidstrich Permanent Makeup (eyeliner)</li>
      <li>Lip Blushing (lips)</li>
      <li>Lippen Permanent Makeup (lips2)</li>
    </ul>
  </div>
</section>

<div class="view-label view-label--inside">Inside</div>

</body>
</html>
```